Email Signature Block Design for Law Firm

I would like you to create a similar signature block for my law firm . I saw the email signature block attached as image002.png and wanted a similar design for my law firm. I want to be able to swap the portraits for each of my staff from the final design. Our law firm colors are black, gold, white, red.

Law

• i like the red circle in around the photo in the oak ridge guild design. The Tall Cedar Guild desgn is what inspired me to have a signature block design for my firm.

```html
<!DOCTYPE html>
<html lang="en">
<head>
<meta charset="utf-8">
<title>Email Signature – The Harlow Firm</title>
<link rel="stylesheet" href="https://fonts.googleapis.com/css2?family=Bebas+Neue&family=Cinzel:wght@500&family=Quattrocento+Sans&family=Quattrocento&display=swap">
<style>
  :root {
    --black: #000000;
    --white: #ffffff;
    --gold: #d4a43a;
    --red: #d21f26;
    --ink: #111111;
    --grey: #8d8d8d;
    --logo-grey: #3b3b3b;
    --badge-blue: #7cc4de;
    --badge-dark: #2d2d2d;
  }
  html, body {
    margin: 0;
    padding: 0;
    overflow: hidden;
    background: var(--white);
  }
  .signature {
    position: relative;
    width: 1200px;
    height: 400px;
    overflow: hidden;
    background: var(--white);
  }
  .office-scene {
    position: absolute;
    left: 768px;
    top: 30px;
    width: 432px;
    height: 274px;
    background: linear-gradient(90deg, rgba(255,255,255,1) 0%, rgba(226,226,226,0.8) 45%, #e6e6e6 100%);
  }
  .firm-name {
    position: absolute;
    left: 40px;
    top: 34px;
    display: flex;
    align-items: center;
    gap: 12px;
    font-family: "Cinzel", serif;
    font-weight: 500;
    font-size: 22px;
    color: var(--logo-grey);
    letter-spacing: 0.02em;
  }
  .firm-mark {
    width: 34px;
    height: 34px;
    background: var(--gold);
  }
  .awards {
    position: absolute;
    left: 870px;
    top: 29px;
  }
  .person-name {
    position: absolute;
    left: 40px;
    top: 156px;
    margin: 0;
    font-family: "Bebas Neue", sans-serif;
    font-weight: 400;
    font-size: 56px;
    line-height: 1;
    letter-spacing: 0.09em;
    color: var(--ink);
  }
  .person-title {
    position: absolute;
    left: 42px;
    top: 211px;
    margin: 0;
    font-family: "Quattrocento Sans", sans-serif;
    font-size: 19px;
    letter-spacing: 0.16em;
    color: var(--grey);
  }
  .contact-band {
    position: absolute;
    left: 0;
    top: 304px;
    width: 1200px;
    height: 96px;
    background: var(--black);
  }
  .contact-list {
    position: absolute;
    left: 41px;
    top: 310px;
    margin: 0;
    padding: 0;
    list-style: none;
    font-family: "Quattrocento", serif;
    font-size: 21px;
    color: var(--white);
  }
  .contact-list li {
    display: flex;
    align-items: center;
    height: 26px;
  }
  .contact-icon {
    width: 14px;
    height: 14px;
    margin-right: 13px;
    flex: none;
  }
  .social-mark {
    width: 10px;
    height: 10px;
    margin: 0 15px 0 2px;
    border: 1.5px solid var(--gold);
    border-radius: 2px;
  }
  .address {
    position: absolute;
    right: 24px;
    top: 326px;
    margin: 0;
    font-family: "Quattrocento", serif;
    font-style: normal;
    font-size: 20px;
    line-height: 27px;
    text-align: right;
    color: var(--white);
  }
  .portrait {
    position: absolute;
    left: 441px;
    top: 40px;
  }
</style>
</head>
<body>
<div class="signature">
  <div class="office-scene" role="img" aria-label="Faded photograph of the firm's office building"></div>

  <div class="firm-name"><span class="firm-mark"></span>The Harlow Firm, PLLC</div>

  <svg class="awards" width="300" height="52" viewBox="0 0 300 52" aria-hidden="true">
    <rect x="0" y="4" width="147" height="44" rx="4" fill="var(--badge-blue)" opacity="0.75"/>
    <rect x="162" y="4" width="76" height="44" rx="4" fill="var(--badge-dark)"/>
    <circle cx="276" cy="26" r="23" fill="var(--badge-dark)"/>
  </svg>

  <h1 class="person-name">Marcus Harlow</h1>
  <p class="person-title">TITLE</p>

  <div class="contact-band"></div>

  <ul class="contact-list">
    <li>
      <svg class="contact-icon" viewBox="0 0 16 16" aria-hidden="true">
        <path d="M3.2 1.5 5.6 1l1.3 3.2-1.6 1.2a8 8 0 0 0 5.3 5.3l1.2-1.6L15 10.4l-.5 2.4c-.2.8-1 1.3-1.8 1.2C6.8 13.4 2.6 9.2 2 3.3c-.1-.8.4-1.6 1.2-1.8Z" fill="var(--gold)"/>
      </svg>
      205-555-0148
    </li>
    <li>
      <svg class="contact-icon" viewBox="0 0 16 16" aria-hidden="true">
        <rect x="1" y="3" width="14" height="10" fill="var(--gold)"/>
        <path d="M1 3.5 8 9l7-5.5" fill="none" stroke="var(--black)" stroke-width="1.2"/>
      </svg>
      contact@harlow-firm.com
    </li>
    <li>
      <span class="social-mark" aria-hidden="true"></span>
      harlowfirmlaw
    </li>
  </ul>

  <address class="address">412 Harbor Row St, Pensacola<br>Florida 32501, US</address>

  <svg class="portrait" width="318" height="318" viewBox="0 0 318 318">
    <defs>
      <linearGradient id="portrait-tone" x1="0" y1="0" x2="0" y2="1">
        <stop offset="0" stop-color="#f4f4f4"/>
        <stop offset="0.5" stop-color="#8a5a45"/>
        <stop offset="1" stop-color="#22252e"/>
      </linearGradient>
    </defs>
    <circle cx="159" cy="159" r="140" fill="url(#portrait-tone)" role="img" aria-label="Staff member portrait photo"/>
    <circle cx="159" cy="159" r="149.5" fill="none" stroke="var(--red)" stroke-width="19"/>
  </svg>
</div>
</body>
</html>
```